Castlereagh Yard Works L.L.C.
Repair Maintenance Improvement
Professional
Patrick Dunleavy
do not want address
pat@castlereaghyardworks.example
Thank You!
The finest compliment I could ever receive is a referral from my friends and customers.

```html
<!DOCTYPE html>
<html lang="en">
<head>
<meta charset="utf-8">
<title>Castlereagh Yard Works L.L.C. — Stationery Set</title>
<link href="https://fonts.googleapis.com/css2?family=Cinzel:wght@600&family=Lato:wght@400;700&display=swap" rel="stylesheet">
<style>
  :root {
    --backdrop: #3b3c3c;
    --paper: #ffffff;
    --paper-shade: #ededed;
    --brand-green: #4b6b63;
    --brand-green-dark: #3f5d56;
    --ink: #4a4f4e;
    --ink-soft: #8a8f8e;
  }
  * { box-sizing: border-box; margin: 0; padding: 0; }
  html, body { width: 1200px; height: 408px; overflow: hidden; background: var(--backdrop); }
  .board { position: relative; width: 1200px; height: 408px; font-family: "Lato", sans-serif; color: var(--ink); }
  .sheet { position: absolute; background: var(--paper); box-shadow: 0 2px 6px rgba(0,0,0,.35); overflow: hidden; }

  .wordmark { display: flex; align-items: center; gap: 5px; font-family: "Cinzel", serif; font-weight: 600; color: var(--brand-green); line-height: 1; white-space: nowrap; }
  .wordmark .mark-square { width: 6px; height: 6px; background: var(--brand-green); flex: none; }
  .wordmark-sm { font-size: 7px; }
  .wordmark-xs { font-size: 5.5px; }
  .tagline { font-family: "Lato", sans-serif; font-size: 3.6px; letter-spacing: .4px; text-transform: uppercase; color: var(--ink-soft); margin-top: 2px; }

  .band { position: absolute; left: 0; right: 0; bottom: 0; background: var(--brand-green); }
  .footer-line { position: absolute; font-size: 3.6px; color: var(--ink-soft); letter-spacing: .2px; }

  /* letterheads */
  .letterhead { top: 22px; width: 160px; height: 372px; }
  .letterhead-one { left: 125px; }
  .letterhead-two { left: 305px; }
  .letterhead .brand-block { position: absolute; top: 12px; left: 14px; }
  .letterhead .band { height: 8px; }
  .letterhead .footer-line { left: 14px; bottom: 12px; }

  /* envelope front */
  .envelope-front { left: 590px; top: 22px; width: 281px; height: 96px; }
  .envelope-front .brand-block { position: absolute; top: 10px; left: 12px; }
  .envelope-front .sender { position: absolute; top: 12px; right: 12px; text-align: right; }
  .sender-name { font-family: "Cinzel", serif; font-weight: 600; font-size: 7px; color: var(--brand-green); letter-spacing: .5px; }
  .sender-contact { font-size: 3.8px; color: var(--ink-soft); margin-top: 2px; }
  .envelope-front .band { height: 6px; }

  /* envelope back */
  .envelope-back { left: 590px; top: 126px; width: 281px; height: 62px; background: var(--brand-green); }
  .envelope-back svg { position: absolute; inset: 0; }

  /* envelope with flap */
  .envelope-flap { left: 590px; top: 225px; width: 281px; height: 145px; }
  .envelope-flap svg { position: absolute; inset: 0; }
  .envelope-flap .brand-block { position: absolute; top: 14px; left: 50%; transform: translateX(-50%); text-align: center; }
  .envelope-flap .brand-block .wordmark { justify-content: center; }

  /* business card */
  .business-card { left: 974px; top: 96px; width: 72px; height: 29px; border-radius: 3px; background: var(--paper-shade); }
  .business-card .band { height: 4px; }
  .business-card .brand-block { position: absolute; top: 7px; left: 6px; }

  /* thank-you cards */
  .thanks-card { top: 137px; height: 48px; border-radius: 3px; padding: 8px 8px; }
  .thanks-card-green { left: 907px; width: 91px; background: var(--brand-green-dark); color: var(--paper); }
  .thanks-card-light { left: 1010px; width: 108px; background: var(--paper-shade); color: var(--brand-green); }
  .thanks-title { font-family: "Cinzel", serif; font-weight: 600; font-size: 7.5px; text-align: right; }
  .thanks-note { font-size: 3.4px; line-height: 1.35; margin-top: 4px; text-align: right; }

  /* note card */
  .note-card { left: 893px; top: 233px; width: 230px; height: 139px; }
  .note-card .brand-block { position: absolute; top: 12px; left: 14px; }
  .note-card .band { height: 7px; }
  .note-card .footer-line { right: 14px; bottom: 12px; }
</style>
</head>
<body>
<main class="board">

  <section class="sheet letterhead letterhead-one">
    <div class="brand-block">
      <div class="wordmark wordmark-sm"><span class="mark-square"></span>Castlereagh Yard Works L.L.C.</div>
      <div class="tagline">Repair Maintenance Improvement</div>
    </div>
    <div class="footer-line">pat@castlereaghyardworks.example</div>
    <div class="band"></div>
  </section>

  <section class="sheet letterhead letterhead-two">
    <div class="brand-block">
      <div class="wordmark wordmark-sm"><span class="mark-square"></span>Castlereagh Yard Works L.L.C.</div>
      <div class="tagline">Repair Maintenance Improvement</div>
    </div>
    <div class="footer-line">pat@castlereaghyardworks.example</div>
    <div class="band"></div>
  </section>

  <section class="sheet envelope-front">
    <div class="brand-block">
      <div class="wordmark wordmark-sm"><span class="mark-square"></span>Castlereagh Yard Works L.L.C.</div>
      <div class="tagline">Repair Maintenance Improvement</div>
    </div>
    <div class="sender">
      <div class="sender-name">PATRICK DUNLEAVY</div>
      <div class="sender-contact">pat@castlereaghyardworks.example</div>
    </div>
    <div class="band"></div>
  </section>

  <section class="sheet envelope-back">
    <svg width="281" height="62" viewBox="0 0 281 62">
      <polygon points="0,0 281,0 140.5,34" fill="#ffffff" opacity="0.92"/>
      <line x1="0" y1="62" x2="120" y2="26" stroke="#ffffff" stroke-opacity=".25" stroke-width="1"/>
      <line x1="281" y1="62" x2="161" y2="26" stroke="#ffffff" stroke-opacity=".25" stroke-width="1"/>
    </svg>
  </section>

  <section class="sheet envelope-flap">
    <svg width="281" height="145" viewBox="0 0 281 145">
      <polyline points="0,0 140.5,62 281,0" fill="none" stroke="#d6d8d7" stroke-width="1"/>
      <line x1="0" y1="145" x2="118" y2="78" stroke="#e3e5e4" stroke-width="1"/>
      <line x1="281" y1="145" x2="163" y2="78" stroke="#e3e5e4" stroke-width="1"/>
    </svg>
    <div class="brand-block">
      <div class="wordmark wordmark-sm"><span class="mark-square"></span>Castlereagh Yard Works L.L.C.</div>
      <div class="tagline">Repair Maintenance Improvement</div>
    </div>
  </section>

  <section class="sheet business-card">
    <div class="brand-block">
      <div class="wordmark wordmark-xs">Castlereagh Yard Works</div>
    </div>
    <div class="band"></div>
  </section>

  <section class="sheet thanks-card thanks-card-green">
    <div class="thanks-title">Thank You!</div>
    <p class="thanks-note">The finest compliment I could ever receive is a referral from my friends and customers.</p>
  </section>

  <section class="sheet thanks-card thanks-card-light">
    <div class="thanks-title">Thank You!</div>
    <p class="thanks-note">The finest compliment I could ever receive is a referral from my friends and customers.</p>
  </section>

  <section class="sheet note-card">
    <div class="brand-block">
      <div class="wordmark wordmark-sm"><span class="mark-square"></span>Castlereagh Yard Works L.L.C.</div>
      <div class="tagline">Repair Maintenance Improvement</div>
    </div>
    <div class="footer-line">pat@castlereaghyardworks.example</div>
    <div class="band"></div>
  </section>

</main>
</body>
</html>
```